Gift Voucher For Medical Cosmetic Clinic

I need a high end, beautiful gift voucher for my Cosmetic Medical Clinic that I will provide to customers in a beautifully designed envelope. I like the colours blue with different tones of blue, white and silver. I have attached my business card for further information.
The address is: 3/14 Dunmore Lane, Ferrymead, Christchurch 8023.
Phone: 0800-457-839
Email: mirel@tovanu.co.nz
Website: www.tovanu.co.nz

```html
<!DOCTYPE html>
<html lang="en">
<head>
<meta charset="utf-8">
<title>Tovanu Gift Voucher and Envelope</title>
<link rel="stylesheet" href="https://fonts.googleapis.com/css2?family=Arimo:wght@400&family=Roboto+Condensed:wght@400&family=Cinzel:wght@400&display=swap">
<style>
  :root {
    --backdrop: #2a2a2a;
    --blue-light: #56b4e7;
    --blue-mid: #2f8bcb;
    --blue-deep: #0a6db4;
    --silver-dark: #b9b8ba;
    --silver-light: #f4f4f5;
    --white: #ffffff;
    --ink: #1b1b1b;
    --logo-silver: #e9ecef;
  }
  * { margin: 0; padding: 0; box-sizing: border-box; }
  html, body {
    width: 1183px; height: 1200px; overflow: hidden;
    background: var(--backdrop);
  }
  .canvas { position: relative; width: 1183px; height: 1200px; }

  .voucher, .envelope {
    position: absolute; left: 105px; width: 973px; height: 486px; overflow: hidden;
    background: linear-gradient(90deg, var(--blue-light) 0%, var(--blue-mid) 55%, var(--blue-deep) 100%);
  }
  .voucher { top: 76px; }
  .envelope { top: 638px; }

  .brand-block {
    position: absolute; display: flex; align-items: center;
    background: linear-gradient(90deg, rgba(86,180,231,0.9), rgba(47,139,203,0.9));
  }
  .brand-block .mark {
    border-radius: 50%;
    border: 3px solid var(--logo-silver);
    flex: none;
  }
  .brand-block .name {
    font-family: "Cinzel", serif; font-weight: 400; color: var(--logo-silver);
    letter-spacing: 0.06em; line-height: 1;
  }
  .voucher .brand-block { left: 55px; top: 44px; width: 403px; height: 120px; padding-left: 28px; gap: 30px; }
  .voucher .brand-block .mark { width: 96px; height: 96px; }
  .voucher .brand-block .name { font-size: 66px; }

  .silver-band {
    position: absolute; left: 0; top: 258px; width: 100%; height: 228px;
    background: linear-gradient(180deg,
      var(--silver-dark) 0%, var(--silver-light) 19%, var(--white) 24%,
      #d6d5d7 50%, #c3c2c4 62%, #e6e6e7 85%, var(--white) 100%);
  }
  .silver-band .headline-strip {
    position: absolute; left: 0; top: 0; width: 100%; height: 43px;
    background: linear-gradient(90deg, #d9d9da 0%, #f6f6f6 30%, #b8b7b9 55%, #f2f2f2 80%, #cfcfd0 100%);
  }
  .headline {
    position: absolute; left: 38px; top: 8px;
    font-family: "Arimo", sans-serif; font-size: 26px; color: var(--ink); letter-spacing: 0.01em;
  }
  .services {
    position: absolute; left: 38px; list-style: none;
    font-family: "Roboto Condensed", sans-serif; font-size: 21px; color: var(--ink);
    display: flex; gap: 12px;
  }
  .services li { display: flex; align-items: center; }
  .services li::before { content: "✓"; width: 40px; font-size: 20px; }
  .services.row-one { top: 89px; }
  .services.row-two { top: 136px; }

  .bow-art {
    position: absolute; left: 622px; top: 215px; width: 325px; height: 259px;
  }

  .envelope-flap {
    position: absolute; left: 0; top: 0; width: 100%; height: 146px;
    border-radius: 0 0 72px 72px;
    background: linear-gradient(90deg, var(--blue-deep) 0%, var(--blue-mid) 50%, var(--blue-light) 100%);
    box-shadow: 0 3px 8px rgba(0,40,90,0.35);
  }
  .envelope .brand-block { left: 386px; top: 49px; width: 202px; height: 60px; padding-left: 14px; gap: 14px; }
  .envelope .brand-block .mark { width: 48px; height: 48px; border-width: 2px; }
  .envelope .brand-block .name { font-size: 33px; }
</style>
</head>
<body>
<main class="canvas">

  <section class="voucher" aria-label="Gift voucher">
    <div class="brand-block">
      <span class="mark"></span>
      <span class="name">TOVANU</span>
    </div>

    <div class="silver-band">
      <div class="headline-strip">
        <h1 class="headline">TOVANU- YOUR LOCAL COSMETIC CLINIC</h1>
      </div>
      <ul class="services row-one">
        <li>Dermal Injectables</li>
        <li>Plasma Facials</li>
        <li>Microneedling</li>
      </ul>
      <ul class="services row-two">
        <li>Skin Boosters</li>
        <li>Excessive Sweating</li>
      </ul>
    </div>

    <svg class="bow-art" viewBox="0 0 325 259" role="img" aria-label="Silver satin gift bow tied across the ribbon band">
      <defs>
        <radialGradient id="bow-tone" cx="50%" cy="40%" r="65%">
          <stop offset="0%" stop-color="#f7f8f8"/>
          <stop offset="60%" stop-color="#dfe2e3"/>
          <stop offset="100%" stop-color="#c4c9ca"/>
        </radialGradient>
      </defs>
      <rect x="0" y="0" width="325" height="259" rx="40" fill="url(#bow-tone)"/>
    </svg>
  </section>

  <section class="envelope" aria-label="Envelope">
    <div class="envelope-flap">
      <div class="brand-block">
        <span class="mark"></span>
        <span class="name">TOVANU</span>
      </div>
    </div>
  </section>

</main>
</body>
</html>
```